Redesign projects page on UK roofing website

Hi guys,

We would like to redesign the projects page of our roofing company website; https://www.brindlecoverings.com/projects

We would like to keep the top of the page the same (up to the big image). Also the footer design should remain the same.

We would like to have some nice photos of work we have done with a little bit of writing about each project.

This site has a nice projects page layout; https://www.tmwbuild.com/projects

Something along those lines would work well for our needs.

Thanks

```html
<!DOCTYPE html>
<html lang="en">
<head>
<meta charset="utf-8">
<title>Projects | Brindle Coverings</title>
<link rel="stylesheet" href="https://fonts.googleapis.com/css2?family=Signika:wght@300;400;600;700&family=Montserrat:wght@400;500&display=swap">
<style>
  :root {
    --brand: #16b0e0;
    --ink: #1c1c1c;
    --muted: #8a8a8a;
    --footer: #0d4a80;
    --footer-line: #2a6398;
    --white: #ffffff;
  }
  * { margin: 0; padding: 0; box-sizing: border-box; }
  html, body { width: 1200px; height: 3341px; overflow: hidden; }
  body { position: relative; background: var(--white); font-family: "Signika", sans-serif; color: var(--ink); }

  .hero {
    position: absolute; left: 0; top: 0; width: 1200px; height: 566px;
    background: linear-gradient(160deg, #3c3c3c 0%, #8d8d8d 35%, #5a5a5a 60%, #9a9a9a 80%, #4a4a4a 100%);
  }
  .site-header { position: absolute; left: 0; top: 0; width: 1200px; height: 90px; }
  .brand { position: absolute; left: 100px; top: 26px; display: flex; align-items: center; gap: 10px; color: var(--white); font-size: 30px; font-weight: 600; }
  .brand .mark { width: 34px; height: 34px; border-radius: 50%; background: var(--brand); }
  .nav { position: absolute; top: 32px; left: 0; list-style: none; }
  .nav li { position: absolute; font-size: 19px; color: var(--white); font-weight: 300; white-space: nowrap; }
  .nav li.active::after { content: ""; position: absolute; left: 0; right: 0; top: 30px; height: 3px; background: var(--brand); }
  .quote-btn { position: absolute; left: 943px; top: 18px; width: 158px; height: 52px; background: var(--brand); color: var(--white); font-size: 19px; font-weight: 600; display: flex; align-items: center; justify-content: center; }

  .hero-title { position: absolute; left: 100px; top: 212px; font-size: 70px; line-height: 78px; font-weight: 700; color: var(--white); }
  .hero-title span { color: var(--brand); }
  .hero-aside { position: absolute; left: 836px; top: 220px; height: 202px; border-left: 3px solid var(--brand); padding-left: 18px; color: var(--white); }
  .hero-aside h2 { font-size: 36px; line-height: 48px; font-weight: 600; }
  .hero-aside p { margin-top: 14px; font-size: 13px; line-height: 22px; font-weight: 600; width: 140px; }

  .section-title { position: absolute; left: 84px; top: 636px; border-left: 4px solid var(--brand); padding-left: 12px; font-size: 44px; font-weight: 400; line-height: 48px; }

  .project { position: absolute; left: 100px; width: 1030px; height: 610px; }
  .project h3 { position: absolute; left: 0; top: 0; font-size: 32px; font-weight: 400; color: var(--brand); }
  .meta { position: absolute; top: 52px; left: 0; width: 1000px; font-size: 23px; }
  .meta span { position: absolute; white-space: nowrap; }
  .meta small { font-size: 16px; font-weight: 300; }
  .project h4 { position: absolute; left: -2px; top: 106px; font-size: 23px; font-weight: 400; }
  .project p { position: absolute; left: 2px; top: 150px; width: 1020px; font-size: 13px; line-height: 22px; color: var(--muted); font-weight: 300; }
  .project .photo { position: absolute; left: 2px; top: 274px; width: 1001px; height: 331px; border-radius: 5px; }

  .learn-more { position: absolute; left: 508px; top: 2829px; width: 184px; height: 66px; background: var(--brand); color: var(--white); font-size: 25px; font-weight: 300; display: flex; align-items: center; justify-content: center; }

  .site-footer { position: absolute; left: 0; top: 2960px; width: 1200px; height: 381px; background: var(--footer); color: var(--white); font-family: "Montserrat", sans-serif; }
  .footer-col { position: absolute; top: 54px; list-style: none; }
  .footer-col h5 { font-family: "Signika", sans-serif; font-size: 18px; font-weight: 400; margin-bottom: 14px; }
  .footer-col li { font-size: 11px; height: 35.5px; }
  .footer-col .sub { margin-top: 6px; }
  .social { display: flex; align-items: center; gap: 8px; }
  .social i { width: 12px; height: 12px; background: var(--white); display: block; }
  .footer-brand { position: absolute; left: 695px; top: 48px; width: 420px; }
  .footer-brand .brand { position: static; font-size: 30px; }
  .footer-brand p { font-size: 11px; line-height: 14px; margin-top: 6px; }
  .badges { position: absolute; left: 695px; top: 186px; display: flex; gap: 22px; align-items: center; }
  .badge { background: rgba(255,255,255,0.85); }
  .footer-rule { position: absolute; left: 105px; right: 100px; top: 333px; height: 1px; background: var(--footer-line); }
  .copyright { position: absolute; left: 105px; top: 352px; font-size: 11px; }
</style>
</head>
<body>
  <section class="hero">
    <div role="img" aria-label="Black and white photo of a corrugated metal roof on an industrial building" style="position:absolute;inset:0"></div>
    <header class="site-header">
      <div class="brand"><i class="mark"></i>brindlecoverings</div>
      <ul class="nav">
        <li style="left:425px">Services</li>
        <li style="left:527px">Clients</li>
        <li class="active" style="left:621px">Projects</li>
        <li style="left:717px">Team</li>
        <li style="left:802px">Contact</li>
      </ul>
      <a class="quote-btn">Get a quote</a>
    </header>
    <h1 class="hero-title">Some of our <span>Latest<br>Projects.</span></h1>
    <div class="hero-aside">
      <h2>What we're<br>working on</h2>
      <p>Keep an eye on some of the latest installs, refurbs and repairs we've carried out.</p>
    </div>
  </section>

  <h2 class="section-title">Roofing Projects</h2>

  <article class="project" style="top:735px">
    <h3>Private Watford</h3>
    <div class="meta">
      <span style="left:0">Type : <small>Single-ply (Tervan S)</small></span>
      <span style="left:313px">Roof Size <small>: 120m2</small></span>
      <span style="left:553px">Date of Completion: <small>January, 2021</small></span>
    </div>
    <h4>Contract Description</h4>
    <p>The client contacted Brindle after a night of very high winds and rain which had caused their EPDM roof to blow off.&nbsp; When Brindle engineers arrived on-site they were shocked to see the EPDM roof and underlying roof deck hanging from a thread in front of the house.&nbsp; Luckily no one was injured and Brindle were able to safely remove the existing roof and install a brand new Tervan single ply roof which was covered by a 15 year manufacturer guarantee.</p>
    <div class="photo" role="img" aria-label="Photo of a newly laid grey single-ply flat roof with terraced houses and trees beyond" style="background:linear-gradient(180deg,#b9bcc0 0%,#6c6f66 35%,#4a5040 50%,#a9b0b8 70%,#c8ccd2 100%)"></div>
  </article>

  <article class="project" style="top:1446px">
    <h3>Sagebrook Kitchens, Billericay</h3>
    <div class="meta">
      <span style="left:0">Type : <small>Insulated Composite Panels</small></span>
      <span style="left:313px">Roof Size <small>: 900m2</small></span>
      <span style="left:553px">Date of Completion: <small>January, 2021</small></span>
    </div>
    <h4>Contract Description</h4>
    <p>Sagebrook Kitchens is a bespoke kitchen design business based in Essex.&nbsp; They contacted Brindle in November 2020 to provide a quote for removal and disposal of their existing asbestos roof and installation of a new energy efficient insulated steel roof.&nbsp; The existing roof incorporated Georgian Wired glass panels installed on an aluminium frame through the centre of the roof.&nbsp; The client required all glass removed and replaced with 32 double skin GRP translucent rooflights.&nbsp; The client also required the works to be completed over the Christmas period when the warehouse was vacant.</p>
    <div class="photo" role="img" aria-label="Photo of new profiled steel roof panels above a dark flat roof" style="background:linear-gradient(180deg,#c9d2dc 0%,#98a6b6 40%,#7d8a98 60%,#3c3c3c 70%,#5a5858 100%)"></div>
  </article>

  <article class="project" style="top:2156px">
    <h3>Renwick Road, Barking</h3>
    <div class="meta">
      <span style="left:0">Type : <small>Single Skin Overclad</small></span>
      <span style="left:313px">Roof Size <small>: 120m2</small></span>
      <span style="left:553px">Date of Completion: <small>October, 2020</small></span>
    </div>
    <h4>Contract Description</h4>
    <p>Our client was looking to convert this extensive property into a place of worship for the incoming tenant.&nbsp; Our client's budget required a cost effective yet efficient solution in order to achieve a guaranteed, watertight building.&nbsp; Our initial survey of the roof exposed a very fragile roof with broken asbestos sheets and multiple leaks on the box gutters. Brindle was able to propose an overlay with new profiled plastisol coated steel sheets and mineral wool insulation, leaving the existing Asbestos cement sheets in-situ.&nbsp; In addition all box gutters were re-lined with Tervan single ply system.</p>
    <div class="photo" role="img" aria-label="Aerial photo of a large industrial building with new pitched steel roofs" style="background:linear-gradient(90deg,#5e6468 0%,#8b949c 35%,#b8c2cc 55%,#6f757a 80%,#4e5256 100%)"></div>
  </article>

  <a class="learn-more">Learn more</a>

  <footer class="site-footer">
    <ul class="footer-col" style="left:105px">
      <h5>Overview</h5>
      <li>Services</li><li>Clients</li><li>Projects</li><li>Team</li><li>Contact</li>
    </ul>
    <ul class="footer-col" style="left:270px">
      <h5>Services</h5>
      <li>Asbestos roof removal</li><li>Steel cladding</li><li>Liquid waterproofing</li><li>Mastic asphalt roofing</li><li>Single ply roofing</li><li>Roof repairs</li><li>Emergency roof repairs</li>
    </ul>
    <ul class="footer-col" style="left:446px">
      <h5>Legal</h5>
      <li>Terms of service</li>
      <h5 class="sub">Follow us</h5>
      <li class="social"><i></i>Network</li>
      <li class="social"><i></i>Gallery</li>
    </ul>
    <div class="footer-brand">
      <div class="brand"><i class="mark"></i>brindlecoverings</div>
      <p>Brindle Coverings Ltd is registered in England as a private limited company.</p>
      <p>Registration No: 07714529</p>
      <p>Registered Office: Unit 14 Marlow Yard, Ferris Lane, Hatfield Heath,<br>Essex CM22 7QT</p>
    </div>
    <div class="badges">
      <div class="badge" style="width:102px;height:38px;border-radius:3px"></div>
      <div class="badge" style="width:72px;height:44px;border-radius:3px"></div>
      <div class="badge" style="width:56px;height:56px;border-radius:50%"></div>
      <div class="badge" style="width:106px;height:40px;border-radius:3px"></div>
    </div>
    <div class="footer-rule"></div>
    <p class="copyright">© Copyright Brindle Coverings Ltd 2023 | All rights reserved.</p>
  </footer>
</body>
</html>
```